Design Project for Digital Recruitment Business

I am launching a new website in the Digital Marketing Recruitment space here in the UK.We are a start up so this very much phase 1 with our web offering.

Key points:

- I think it will be aproximately 5- 8 pages

- I am looking for wordpress(open on this)) design and coding/ development.

- It really is going to be a brochure site on the whole so don't expect any huge integration. I would like an RSS feed to publish our jobs on our site. I can get the code for that from my recruitment database partner Quillpost, all i will need is a blank page for that section?.Parley net,chirrup etc as well.

-I already have the logo.(See attached)which you guys delivered brilliantly on :-)

some reference sites I like the look of: http://www.orbitvale.example.co.uk http://www.ratchethouse.example.com/ http://www.webmavens.example.co.uk/

The menu bar on these sites are good, the language is good.I want contemporary and professional.It needs to connect to the viewer.
WE are in the social media space so that needs to fit/blend eg parleynet,GS.

SUGGESTED APPROACH
So I guess the best starting point would be to just submit a home page design so i can judge the styles I like best.Then the finalists of that round can submit another section of the website to see the consistency in terms of look and feel. I will then pick someone to work one on one with to complete the design and do the coding. That way no one gets to waste valuable time and energy :-)

Feel free to ping me questions
Updates

Reason: Hello All, I am going to extend by a few days. I have been inundated with work.However I Plan to look at all your designs this week end and respond to all your Queries. Thanks for your Patience.

Hi guys

here is a little more about us

We know that the career success of the candidates we place can have a great impact on the success of your business. We have built a network of talented industry professionals and an extensive knowledge of the market and its changing trends. We focus on career management,advice and consultancy.With over 30 years experience in our team we feel confident we can deliver. Our specialisms are Creative and Design,Digital Marketing,Editorial and Content,User Experience,and Technology related to building Websites.

In today's world of continually adapting,surviving and thriving we recognise that you rise and fall by the people you hire.That is why an expert  is required to help find those people in business critical roles. So if your online Marketing strategy is behind the times or your website traffic is poor for example we can help find people on a contract and permanent basis to bridge the gap in you marketing and E-commerce team. Pixel Scouts are specialists in these areas and offer a consultative approach to working with your business. If your business grows as a result of the people you recruited through us we could not be happier. Honest,straightforward,professional.

In terms of home page the Menu bar is 4-5 topics at most. 90% of the traffic to this website will be Candidates so Jobs will be the best content along with the 6 skill sets/categories and everything social after that.Very like Ratchet website I mentioned in the Brief. A couple of you are on the right tracks.
Hope this helps for now. I feel confident I can pick from one of you.

Kind regards

Martin

Soory one other thing,

RE; Images

People are tricky to do on Recruitment websites as its very PC and they dont look real enough.Animations of people are better in my humble opinion...

open to ideas/options

Thanks

Target Market(s)

marketeers,designers,ecommerce folks.

Industry/Entity Type

Business

Requirements
Must have
• open at this stage but obviously the logo design colours must sync with the overall look and feel.GS,chirrup,mingle+ must be dominant

```html
<!DOCTYPE html>
<html lang="en">
<head>
<meta charset="utf-8">
<title>Pixel Scouts – Digital Recruitment</title>
<link href="https://fonts.googleapis.com/css2?family=Source+Sans+3:wght@400;600;700&family=Arvo&display=swap" rel="stylesheet">
<style>
:root{
  --orange:#f26415;
  --orange-dark:#e04e08;
  --red:#d8161d;
  --purple:#4a2a86;
  --blue:#1c8fd6;
  --navy:#1d4f8c;
  --text:#444;
  --footer:#1b1b1b;
  --footer-base:#101010;
}
*{box-sizing:border-box;margin:0;padding:0}
html,body{width:927px;height:1200px;overflow:hidden;background:#fff}
body{position:relative;font-family:"Source Sans 3",sans-serif;color:var(--text)}
.abs{position:absolute}
a{color:inherit;text-decoration:none}

/* header */
.header{left:0;top:0;width:927px;height:110px;background:linear-gradient(#fafafa,#eee)}
.brand{left:45px;top:30px;display:flex;align-items:center;gap:8px}
.brand-dot{width:28px;height:28px;border-radius:50%;background:var(--orange)}
.brand-name{font-size:30px;font-weight:700;color:var(--orange);letter-spacing:-.5px}
.nav-tab{left:413px;top:0;width:65px;height:110px;background:#fff}
.nav{top:51px;font-size:13px;color:#333;letter-spacing:.2px}

/* sub bar */
.subbar{left:0;top:110px;width:927px;height:52px;background:linear-gradient(var(--orange),var(--orange-dark))}
.sub{top:128px;font-size:12px;color:#3a1200;font-weight:400;letter-spacing:.2px}
.sep{top:114px;width:1px;height:44px;background:rgba(255,255,255,.35)}
.search{left:499px;top:118px;width:406px;height:38px;background:#fff;border-radius:3px}
.search svg{position:absolute;left:10px;top:6px}
.search-label{position:absolute;left:47px;top:12px;font-size:10.5px;color:#999;letter-spacing:.3px}
.search-btn{position:absolute;right:6px;top:4px;width:73px;height:30px;border-radius:4px;background:linear-gradient(#f7833a,#e4500c);border:1px solid #c84306;color:#fff;font-size:13px;font-weight:400;text-align:center;line-height:28px}

/* slider */
.slider{left:25px;top:174px;width:871px;height:322px;border:1px solid #eee;background:#fbfbfb}
.slide{left:41px;top:188px;width:839px;height:293px;border:2px solid #ddd;background:linear-gradient(#fff,#f4f4f4)}
.art-left{left:54px;top:217px;width:190px;height:249px;background:#ececec}
.art-right{left:640px;top:240px;width:230px;height:208px;background:#ebe6e3}
.slide-title{left:261px;top:252px;font-size:18px;color:#222;font-weight:400}
.slide-title span{color:var(--red)}
.slide-copy{left:262px;top:302px;width:365px;font-size:11.5px;line-height:18px;color:#222}
.dots{left:461px;top:485px;display:flex;gap:5px}
.dots i{width:9px;height:9px;border-radius:50%;background:#999;display:block}
.dots i.on{background:var(--red)}

/* features */
.thumb{width:81px;height:73px;border:2px solid #ddd;background:#fff;padding:4px}
.thumb div{width:100%;height:100%}
.feat-title{font-family:"Arvo",serif;font-size:21px;color:var(--purple);top:539px;font-weight:400}
.more{top:580px;height:23px;padding:0 10px;background:#e8e8e8;border-radius:2px;font-size:12px;color:#555;line-height:23px}

/* feeds */
.rss-icon{left:21px;top:689px;width:38px;height:40px;border-radius:7px;background:var(--orange)}
.rss-title{left:66px;top:684px;width:200px;font-size:16px;line-height:27px;color:var(--orange);font-weight:400}
.jobs{left:23px;top:756px;list-style:none;font-size:12px;color:#444}
.jobs li{height:34.3px;display:flex;gap:8px}
.jobs li::before{content:"";width:7px;height:7px;margin-top:4px;border:1px solid #888;background:#eee}
.view-btn{left:153px;top:928px;width:93px;height:27px;border:1px solid #bbb;border-radius:3px;background:linear-gradient(#fff,#e5e5e5);font-size:11px;font-weight:600;color:var(--navy);text-align:center;line-height:25px}
.sq-icon{width:44px;height:45px;border-radius:8px}
.feed-title{top:698px;font-size:16px;letter-spacing:.2px;font-weight:400}
.bubble{left:314px;top:742px;width:279px;height:200px}
.feed-text{font-size:10.5px;line-height:14.5px;color:#666}
.feed-text p{margin-bottom:14px}
.feed-text em{font-style:normal;color:var(--blue)}
.read-more{left:826px;top:941px;font-size:10.5px;color:var(--navy)}

/* footer */
.rule{left:0;top:982px;width:927px;border-top:1px dotted #999}
.footer{left:0;top:986px;width:927px;height:214px;background:linear-gradient(#2a2a2a,var(--footer))}
.f-head{top:1001px;font-size:13px;color:#eee;font-weight:400}
.f-list{top:1031px;list-style:none;font-size:10.5px;line-height:16.3px;color:#bbb}
.f-text{top:1031px;font-size:10.5px;line-height:18px;color:#bbb}
.nl-head{left:691px;top:1010px;font-size:16px;color:#eee;font-weight:400}
.nl-input{left:685px;top:1045px;width:214px;height:33px;border-radius:4px;background:#fff;font-size:10.5px;color:#444;padding:10px 14px}
.nl-btn{left:685px;top:1094px;width:80px;height:25px;border-radius:3px;background:linear-gradient(#e42a2a,#b40f12);color:#fff;font-size:12.5px;font-weight:600;padding:3px 12px}
.base{left:0;top:1138px;width:927px;height:62px;background:var(--footer-base)}
.social{top:1157px;width:31px;height:31px;border-radius:50%;border:2px solid #ddd}
.copy{right:25px;top:1155px;font-size:10.5px;color:#bbb}
</style>
</head>
<body>

<div class="abs header"></div>
<div class="abs brand"><span class="brand-dot"></span><span class="brand-name">pixelscouts</span></div>
<div class="abs nav-tab"></div>
<a class="abs nav" style="left:427px">HOME</a>
<a class="abs nav" style="left:494px">ABOUT US</a>
<a class="abs nav" style="left:583px">CLIENTS</a>
<a class="abs nav" style="left:661px">JOBS</a>
<a class="abs nav" style="left:725px">RESOURCES</a>
<a class="abs nav" style="left:825px">CONTACT US</a>

<div class="abs subbar"></div>
<a class="abs sub" style="left:43px">BROWSE OUR JOBS</a>
<span class="abs sep" style="left:159px"></span>
<a class="abs sub" style="left:177px">MEDIA</a>
<span class="abs sep" style="left:231px"></span>
<a class="abs sub" style="left:250px">CREATIVE MARKETING</a>
<span class="abs sep" style="left:379px"></span>
<a class="abs sub" style="left:401px">CONTENT</a>
<div class="abs search">
  <svg width="30" height="28" viewBox="0 0 30 28"><circle cx="17" cy="11" r="8" fill="none" stroke="#d8161d" stroke-width="4"/><line x1="11" y1="17" x2="3" y2="25" stroke="#d8161d" stroke-width="5" stroke-linecap="round"/></svg>
  <span class="search-label">SEARCH FOR YOUR PERFECT JOB</span>
  <span class="search-btn">SEARCH</span>
</div>

<div class="abs slider"></div>
<div class="abs slide"></div>
<div class="abs art-left" role="img" aria-label="Illustration of two business figures standing back to back"></div>
<div class="abs art-right" role="img" aria-label="Photo of a smiling professional with a team of colleagues behind"></div>
<h1 class="abs slide-title"><span>QUICKER ACCESS</span> to the right talent for you</h1>
<p class="abs slide-copy">Aliquam molestie, mi et imperdiet euismod, dui purus auctor tellus, et interdum lacus lectus et ante. Sed accumsan sollicitudin sapien, sit amet adipiscing turpis gravida ac. In congue, neque nec lobortis volu pat, libero mauris varius mi, vitae suscipit ipsum ligula vitae purus.</p>
<div class="abs dots"><i></i><i></i><i class="on"></i><i></i><i></i></div>

<div class="abs thumb" style="left:20px;top:534px"><div role="img" aria-label="Illustration of a figure climbing a red staircase" style="background:#f1e4e4"></div></div>
<h2 class="abs feat-title" style="left:110px">DREAM JOBS</h2>
<a class="abs more" style="left:110px">View more</a>

<div class="abs thumb" style="left:318px;top:538px"><div role="img" aria-label="Illustration of a figure holding a red sign" style="background:#f3eeee"></div></div>
<h2 class="abs feat-title" style="left:410px">DREAM HIRE</h2>
<a class="abs more" style="left:410px">View more</a>

<div class="abs thumb" style="left:642px;top:538px"><div role="img" aria-label="Illustration of two figures shaking hands on puzzle pieces" style="background:#e3ecef"></div></div>
<h2 class="abs feat-title" style="left:736px">JOIN US</h2>
<a class="abs more" style="left:736px">View more</a>

<div class="abs rss-icon" role="img" aria-label="Job feed icon"></div>
<h3 class="abs rss-title">RSS FEEDS OF LATEST JOB VACANCIES.</h3>
<ul class="abs jobs">
  <li>Ad Operations Manager - Ad Business,</li>
  <li>Agency Sales Account Director - £50k - £75k</li>
  <li>Digital Account Manager - Real Time Bidding</li>
  <li>Agency Sales Account - DMP - £50k - £75k</li>
  <li>Sales Director - Big Data - £75k - £100</li>
</ul>
<a class="abs view-btn">VIEW MORE</a>

<div class="abs sq-icon" style="left:316px;top:688px;background:var(--blue)" role="img" aria-label="chirrup"></div>
<h3 class="abs feed-title" style="left:374px;color:var(--blue)">CHIRRUP FEED</h3>
<svg class="abs bubble" viewBox="0 0 279 200" width="279" height="200">
  <path d="M4 0.5 H275 Q278.5 0.5 278.5 4 V145 Q278.5 148.5 275 148.5 H175 L66 199 L86 148.5 H4 Q0.5 148.5 0.5 145 V4 Q0.5 0.5 4 0.5Z" fill="#fafafa" stroke="#ccc"/>
</svg>
<div class="abs feed-text" style="left:323px;top:759px;width:268px">
  <p>Agency Sales Account Director - DSP - Agency Sales Media jobs - Orbit Talent Recruitment London shrt.example/TilVLZ<br><em>1 hour ago</em></p>
  <p>browse our jobs plnk.example/QGSrKu <em>11 Oct</em></p>
  <p>Our marketing jobs jobs - Orbit Talent Recruitment London shrt.example/Q9E4w9 <em>11 Oct</em></p>
</div>

<div class="abs sq-icon" style="left:640px;top:690px;width:46px;height:46px;background:var(--navy)" role="img" aria-label="parleynet"></div>
<h3 class="abs feed-title" style="left:691px;color:var(--navy)">PARLEYNET FEED</h3>
<div class="abs feed-text" style="left:641px;top:759px;width:250px">
  <p>Agency Sales Account Director - DSP - Agency Sales Media jobs - Orbit Talent Recruitment shrt.example/TilVLZ<br><em>1 hour ago</em></p>
  <p>browse our jobs plnk.example/QGSrKu <em>11 Oct</em></p>
  <p>Our marketing jobs jobs - Orbit Talent Recruitment London shrt.example/Q9E4w9 <em>11 Oct</em></p>
  <p>Our marketing jobs jobs - Orbit Talent Recruitment London shrt.example/Q9E4w9 <em>11 Oct</em></p>
</div>
<a class="abs read-more">READ MORE &gt;&gt;</a>

<div class="abs rule"></div>
<div class="abs footer"></div>
<h4 class="abs f-head" style="left:32px">Browse Jobs</h4>
<ul class="abs f-list" style="left:33px"><li>Media Jobs</li><li>Creative Jobs</li><li>Marketing Jobs</li><li>Content Jobs</li></ul>
<h4 class="abs f-head" style="left:223px">Quick Links</h4>
<ul class="abs f-list" style="left:224px"><li>Send Us Your CV</li><li>Refer a Friend</li><li>Brief Us</li><li>Request A Call</li></ul>
<h4 class="abs f-head" style="left:423px">Contact Us</h4>
<p class="abs f-text" style="left:424px">Sed ut perspiciatis unde omnis iste<br>natus error voluptatem accusantium<br><br>Phone : 555 010 236<br>Email : info@pixelscouts.example.com</p>
<h4 class="abs nl-head">Newsletter</h4>
<div class="abs nl-input">Enter Your Email id</div>
<a class="abs nl-btn">Sign Up</a>

<div class="abs base"></div>
<span class="abs social" style="left:34px;background:#3b5998" role="img" aria-label="GS"></span>
<span class="abs social" style="left:73px;background:var(--blue)" role="img" aria-label="chirrup"></span>
<span class="abs social" style="left:111px;background:var(--navy)" role="img" aria-label="parleynet"></span>
<p class="abs copy">© 2012 pixelscouts, All rights reserved</p>

</body>
</html>
```